Website design for commercial and residential security company

we're looking to see some new designs for an established company with no website.

homepage and one inner page

here is a link to the homepage content, sitemap, logo and more.
https://files.brontavel.net/share/7QxmPzLrTw2vNkdJhYcsa9eFgbUoiVwRn?view=open

call to action should be Request A Quote

if you have any questions please send them to us asap

thank you

1 page

Sans Serif

```html
<!DOCTYPE html>
<html lang="en">
<head>
<meta charset="utf-8">
<title>Brightline Security Solutions — Home</title>
<link rel="stylesheet" href="https://fonts.googleapis.com/css2?family=Montserrat:wght@500;600;700&family=Roboto:wght@400&display=swap">
<style>
:root{
  --gold:#c9a42c;
  --gold-dark:#b8932a;
  --ink:#555555;
  --body:#333333;
  --footer:#262626;
  --white:#ffffff;
}
*{margin:0;padding:0;box-sizing:border-box}
html,body{width:1200px;height:2973px;overflow:hidden;background:var(--white)}
body{position:relative;font-family:Roboto,Arial,sans-serif;color:var(--body)}
.abs{position:absolute}
.head{font-family:Montserrat,Arial,sans-serif}

.top-rule{left:0;top:0;width:1200px;height:4px;background:var(--gold)}
.site-header{left:0;top:4px;width:1200px;height:132px;background:var(--white)}
.brand{display:flex;align-items:center;gap:12px}
.brand-mark{width:30px;height:30px;border-radius:50%;background:var(--gold)}
.brand-name{font-family:Montserrat,sans-serif;font-weight:700;color:#7a7a7a;font-size:30px;letter-spacing:1px}
.site-header .brand{position:absolute;left:112px;top:46px}
.main-nav a{position:absolute;top:60px;font-family:Montserrat,sans-serif;font-weight:500;font-size:14px;color:#444;text-decoration:none;letter-spacing:.3px}
.main-nav a.active{color:var(--gold)}

.hero{left:0;top:136px;width:1200px;height:733px;background:linear-gradient(100deg,#5c5a58 0%,#8a7e6e 35%,#6e6454 60%,#3d3a36 100%)}
.hero-title{left:601px;top:372px;font-family:Montserrat,sans-serif;font-weight:700;font-size:62px;color:var(--white);letter-spacing:1px;text-shadow:0 2px 6px rgba(0,0,0,.35)}
.hero-sub{left:602px;top:452px;width:500px;font-size:25px;line-height:39px;color:var(--white)}
.btn{display:flex;align-items:center;justify-content:center;font-family:Montserrat,sans-serif;font-weight:600;color:var(--white);background:var(--gold);border-radius:32px;text-decoration:none}
.hero-cta{left:603px;top:550px;width:200px;height:63px;font-size:17px}

.mission{left:111px;top:803px;width:978px;height:370px}
.mission-text{left:111px;top:855px;width:978px;text-align:center}
.section-title{font-family:Montserrat,sans-serif;font-weight:700;font-size:36px;color:var(--ink);letter-spacing:.5px}
.title-rule{width:42px;height:3px;background:var(--gold);margin:16px auto 18px}
.lead-gold{font-family:Montserrat,sans-serif;font-weight:500;font-size:16.5px;line-height:29px;color:var(--gold)}
.small-body{font-size:14px;line-height:28px;color:#444;margin-top:16px}

.commercial-text{left:200px;top:1228px;width:800px;text-align:center}
.caps-gold{font-family:Montserrat,sans-serif;font-weight:600;font-size:14.5px;line-height:28px;color:var(--gold);margin-top:26px}
.commercial-text .small-body{font-size:15px;line-height:29px;margin-top:12px}
.commercial-photo{left:111px;top:1471px;width:489px;height:522px;background:linear-gradient(120deg,#e4dccd 0%,#9d9a7e 40%,#3c3d38 70%,#c7bea8 100%)}
.feature-list{left:638px;top:1486px;width:460px;list-style:none}
.feature-list li{position:relative;padding-left:34px;font-size:17.5px;line-height:28px;color:#444;margin-bottom:26px}
.feature-list svg{position:absolute;left:0;top:8px}
.read-more{left:638px;top:1910px;width:177px;height:60px;font-size:17px}

.residential{left:0;top:2079px;width:1200px;height:555px;background:linear-gradient(90deg,#8d6b45 0%,#b9a074 30%,#cdb04e 55%,#c9a93a 100%)}
.residential-photo{left:0;top:2079px;width:640px;height:555px;background:linear-gradient(90deg,rgba(120,80,50,.6),rgba(200,180,120,.2) 80%,rgba(201,169,58,0))}
.res-title{left:643px;top:2150px;font-family:Montserrat,sans-serif;font-weight:600;font-size:37px;line-height:54px;color:var(--white)}
.res-sub{left:643px;top:2266px;width:450px;font-family:Montserrat,sans-serif;font-weight:700;font-size:14.5px;line-height:26px;color:var(--white)}
.res-body{left:643px;top:2357px;width:446px;font-size:14.5px;line-height:27.6px;color:var(--white);text-align:justify}

.site-footer{left:0;top:2634px;width:1200px;height:339px;background:var(--footer)}
.site-footer .brand{position:absolute;left:0;width:1200px;top:70px;justify-content:center}
.site-footer .brand-name{color:#bdbdbd;font-size:40px}
.site-footer .brand-mark{width:40px;height:40px}
.footer-nav a{position:absolute;top:162px;transform:translateX(-50%);font-family:Montserrat,sans-serif;font-weight:500;font-size:14px;color:var(--white);text-decoration:none}
.social{position:absolute;left:495px;top:205px;display:flex;gap:7px}
.social span{width:36px;height:36px;border:2px solid var(--white);border-radius:50%}
.copyright{position:absolute;left:0;top:268px;width:1200px;text-align:center;font-size:16px;color:var(--white)}
</style>
</head>
<body>
<div class="abs top-rule"></div>
<header class="abs site-header">
  <div class="brand"><span class="brand-mark"></span><span class="brand-name">Brightline Security</span></div>
  <nav class="main-nav">
    <a class="active" href="#" style="left:564px">HOME</a>
    <a href="#" style="left:655px">ABOUT</a>
    <a href="#" style="left:752px">SOLUTIONS</a>
    <a href="#" style="left:883px">RESOURCES</a>
    <a href="#" style="left:1020px">CONTACT</a>
  </nav>
</header>

<section class="abs hero" role="img" aria-label="Photo of a hand holding a smart home control phone in a bright living room"></section>
<h1 class="abs hero-title">BRIGHTLINE</h1>
<p class="abs hero-sub">Sed ut perspiciatis unde omnis iste natus err or sit voluptatem accusantium</p>
<a class="abs btn hero-cta" href="#">REQUEST A QUOTE</a>

<svg class="abs mission" viewBox="0 0 978 370" aria-hidden="true">
  <defs><filter id="cardShadow" x="-5%" y="-5%" width="110%" height="115%"><feDropShadow dx="0" dy="4" stdDeviation="6" flood-color="#000" flood-opacity=".12"/></filter></defs>
  <path d="M0 0H978V282Q489 440 0 282Z" fill="#fff" filter="url(#cardShadow)"/>
</svg>
<div class="abs mission-text">
  <h2 class="section-title">OUR MISSION</h2>
  <div class="title-rule"></div>
  <p class="lead-gold">To provide our customers with comprehensive security, audio/video, and automation with<br>top notch customer service. We Ensure Security with Smart Tools.</p>
  <p class="small-body">The graded security measures from Brightline Security Solutions ensure the safety of both residential and commercial<br>property. We provide a wide range of Residential and Commercial Security Solutions.</p>
</div>

<div class="abs commercial-text">
  <h2 class="section-title">COMMERCIAL SOLUTIONS</h2>
  <p class="caps-gold">PROTECT ASSETS AND SECURITY OF YOUR BUSINESS WITH EXCEPTIONAL<br>COMMERCIAL SECURITY INSTALLATION</p>
  <p class="small-body">People's safety is our top priority. This includes ensuring that the security system built at your commercial property is configured accurately. Further, it will protect against intruders, burglaries, and holdups. We do this by:</p>
</div>
<div class="abs commercial-photo" role="img" aria-label="Photo of a finger on a fingerprint access control reader mounted on a glass door"></div>
<ul class="abs feature-list">
  <li><svg width="14" height="14" viewBox="0 0 14 14"><circle cx="7" cy="7" r="6" fill="none" stroke="#c9a42c" stroke-width="1.6"/><path d="M4 7h5M7 4.5 9.5 7 7 9.5" fill="none" stroke="#c9a42c" stroke-width="1.6"/></svg>Audio &amp; Video Solutions for your commercial property</li>
  <li><svg width="14" height="14" viewBox="0 0 14 14"><circle cx="7" cy="7" r="6" fill="none" stroke="#c9a42c" stroke-width="1.6"/><path d="M4 7h5M7 4.5 9.5 7 7 9.5" fill="none" stroke="#c9a42c" stroke-width="1.6"/></svg>Burglar Alarms &amp; Detectors</li>
  <li><svg width="14" height="14" viewBox="0 0 14 14"><circle cx="7" cy="7" r="6" fill="none" stroke="#c9a42c" stroke-width="1.6"/><path d="M4 7h5M7 4.5 9.5 7 7 9.5" fill="none" stroke="#c9a42c" stroke-width="1.6"/></svg>CCTV cameras equipped with facial recognition technologies enable the technology to identify the offenders.</li>
  <li><svg width="14" height="14" viewBox="0 0 14 14"><circle cx="7" cy="7" r="6" fill="none" stroke="#c9a42c" stroke-width="1.6"/><path d="M4 7h5M7 4.5 9.5 7 7 9.5" fill="none" stroke="#c9a42c" stroke-width="1.6"/></svg>Monitoring of alarms and video recordings 24 hours a day, seven days a week. Addressing all the incidents with an urgent response.</li>
  <li><svg width="14" height="14" viewBox="0 0 14 14"><circle cx="7" cy="7" r="6" fill="none" stroke="#c9a42c" stroke-width="1.6"/><path d="M4 7h5M7 4.5 9.5 7 7 9.5" fill="none" stroke="#c9a42c" stroke-width="1.6"/></svg>Alarm systems and cameras precisely installed so that more of your property is tracked.</li>
</ul>
<a class="abs btn read-more" href="#">READ MORE</a>

<section class="abs residential"></section>
<div class="abs residential-photo" role="img" aria-label="Photo of a smiling woman using a home security app on her phone"></div>
<h2 class="abs res-title">RESIDENTIAL<br>SECURITY SOLUTIONS</h2>
<p class="abs res-sub">CONSIDER A HOME SURVEILLANCE DEVICE THAT WOULD DO MORE FOR YOU AND YOUR FAMILY THAN YOU EVER IMAGINED.</p>
<p class="abs res-body">Brightline Security Solutions is your trustable security provider. Also, as certified professionals carry out the installation, you have everything under control. Your home is being securely watched from various points, with cameras capable of tracking any intruder's path. Specifically, we offer Residential Intrusion Detection Security Systems, Residential Alarm, Residential Network Wi-Fi, CCTVs and residential home automation.</p>

<footer class="abs site-footer">
  <div class="brand"><span class="brand-mark"></span><span class="brand-name">Brightline Security</span></div>
  <nav class="footer-nav">
    <a href="#" style="left:345px">HOME</a>
    <a href="#" style="left:447px">ABOUT</a>
    <a href="#" style="left:567px">SOLUTIONS</a>
    <a href="#" style="left:707px">RESOURCES</a>
    <a href="#" style="left:841px">CONTACT</a>
  </nav>
  <div class="social" aria-label="Social links"><span></span><span></span><span></span><span></span><span></span></div>
  <p class="copyright">© Copyrights 2021 Brightline.All Rights Reserved.</p>
</footer>
</body>
</html>
```